Business Cards

Hi,
We are due for an update of bussiness cards. I Hvae also included jpg of our current card with old logo just so you can see why we want change). We do have a current logo (attached) however would like the cards to be more modern and edgy, double sided, with the following words (final to be provided in suitable format for printer):
Below are some of the essentials;

FRONT

KRPVN logo
Learn to Dance
Modern Jive and West Coast Swing
0417 862 551

BACK

Dance, it’s cheaper than therapy!
New Dancers – FREE Entry

```html
<!DOCTYPE html>
<html lang="en">
<head>
<meta charset="utf-8">
<title>Kirra Pivot — Business Cards</title>
<link rel="stylesheet" href="https://fonts.googleapis.com/css2?family=Lato:wght@400;700&display=swap">
<style>
  :root {
    --bg: #2a2d31;
    --card: #0b0b0b;
    --orange: #f28c1e;
    --white: #ffffff;
    --shadow: rgba(0,0,0,0.45);
  }
  * { margin: 0; padding: 0; box-sizing: border-box; }
  html, body { width: 1200px; height: 900px; overflow: hidden; }
  body {
    background: var(--bg);
    font-family: "Lato", sans-serif;
    position: relative;
  }
  .card {
    position: absolute;
    background: var(--card);
    border-radius: 26px;
    overflow: hidden;
    box-shadow: 0 18px 40px var(--shadow);
  }
  .card__corners { position: absolute; inset: 0; }
  .card--front { left: 60px; top: 280px; width: 600px; height: 343px; }
  .card--back  { left: 780px; top: 150px; width: 343px; height: 600px; }

  .brand-name {
    color: var(--orange);
    font-weight: 400;
    white-space: nowrap;
  }

  /* front */
  .front__brand {
    position: absolute;
    left: 60px; top: 0; width: 230px; height: 100%;
    display: flex; align-items: center; justify-content: center;
  }
  .front__brand .brand-name { font-size: 50px; }
  .front__divider {
    position: absolute;
    left: 318px; top: 112px;
    width: 3px; height: 120px;
    background: var(--white);
  }
  .front__details {
    position: absolute;
    right: 34px; top: 92px;
    text-align: right;
  }
  .front__logo-label { color: var(--orange); font-weight: 700; font-size: 26px; line-height: 1.15; }
  .front__tagline { color: var(--white); font-size: 24px; line-height: 1.2; margin-bottom: 12px; }
  .front__info { color: var(--orange); font-size: 15px; line-height: 1.6; }

  /* back */
  .back__brand {
    position: absolute;
    left: 0; right: 0; top: 170px;
    text-align: center;
  }
  .back__brand .brand-name { font-size: 62px; }
  .back__message {
    position: absolute;
    left: 0; right: 0; top: 300px;
    text-align: center;
  }
  .back__slogan { color: var(--orange); font-size: 21px; line-height: 1.4; }
  .back__offer { color: var(--white); font-size: 22px; line-height: 1.4; }
</style>
</head>
<body>

  <section class="card card--front" aria-label="Card front">
    <svg class="card__corners" width="600" height="343" viewBox="0 0 600 343" aria-hidden="true">
      <polygon points="0,0 148,0 0,148" fill="var(--white)"/>
      <polygon points="0,0 134,0 0,134" fill="var(--orange)"/>
      <polygon points="600,343 452,343 600,195" fill="var(--white)"/>
      <polygon points="600,343 466,343 600,209" fill="var(--orange)"/>
    </svg>
    <div class="front__brand"><span class="brand-name">Kirra Pivot</span></div>
    <div class="front__divider"></div>
    <div class="front__details">
      <p class="front__logo-label">KRPVN logo</p>
      <p class="front__tagline">Learn to Dance</p>
      <p class="front__info">Modern Jive and West Coast Swing</p>
      <p class="front__info">www.kirrapivot.com.au</p>
      <p class="front__info">0417 862 551</p>
    </div>
  </section>

  <section class="card card--back" aria-label="Card back">
    <svg class="card__corners" width="343" height="600" viewBox="0 0 343 600" aria-hidden="true">
      <polygon points="0,0 148,0 0,148" fill="var(--white)"/>
      <polygon points="0,0 134,0 0,134" fill="var(--orange)"/>
      <polygon points="343,600 195,600 343,452" fill="var(--white)"/>
      <polygon points="343,600 209,600 343,466" fill="var(--orange)"/>
    </svg>
    <div class="back__brand"><span class="brand-name">Kirra Pivot</span></div>
    <div class="back__message">
      <p class="back__slogan">Dance, it's Caeaper than therapy!</p>
      <p class="back__offer">New Dancer- FREE Entry</p>
    </div>
  </section>

</body>
</html>
```